Book Cover Design - Rooted Together: 7 Paths to Raise a Household that Blooms

International cover needed for the Australian (Fenwick Marlow/QRT Press 2011) non-fiction book Rooted Together: 7 Paths to Raise a Household that Blooms.

Blurb: With the birth of a baby, come other new beginnings, the birth of a mother, of a father, and of a family. With each stage of a child's growth, and with every new baby, there are more new beginnings. In older cultures and in villages around the world, parenthood was considered a rite of passage but traditions that guided parents into becoming a family have largely been lost - until now.

This ground breaking book walks a new generation of mothers and fathers through the eight steps of the modern parenthood rite of passage, from couple-connection to family-foundations, so they can prepare for and continue to grow a family that thrives.

Bio: Nora Pembridge is a relationship counsellor, parent educator and columnist for Homeward Nursery magazine. She lives in Sydney with her husband, their three gorgeous children and an itinerary of pets. This is her first book.
Updates

Thank you for your patience, I haven't ever done anything like this before and the designs submitted have helped me to be more specific in my requests. Please see the updated brief. The most important point is that I am seeking a TEXT based cover, so BOTH the TITLE and SUBTITLE should take up most of the space, the image could either be in the background with the title and subtitle overlayed, or be much smaller to fit around them. I have attached some more images to the brief, hope they help to convey the 'feel' I am after.  Thanks again!

Reason: Thank you so much for taking an interest in this project, the process has been very educational and helpful for me. While some of the stock art in the submitted designs are great, I've decided to commission a custom illustration which completely captures the meaning of Rooted Together. I will upload the illustration once it's complete for designers who are still interested to use. Thank you for your patience! Nora

Thank you all for your patience and for opening up my thinking about what I am really hoping for with this cover. I have uploaded some new tree designs and more specific instructions that I would like to be included in the cover design. I'm looking forward to seeing your creations!

With warm regards,

Nora

Target Market(s)

Couples thinking about having a baby and new parents of one or more young children.

Industry/Entity Type

Baby

Requirements
Must have
• TEXT based cover with BOTH the TITLE and SUBTITLE taking up most of the page.
Colors to match the Australian version (see attached)
Tree design bottom left (as per Trunk Treatment image attached) OR Heart Tree Design
Root design (as per one of the two images attached)
PLEASE ADD: three new shoots coming up from the ground under the tree to symbolize the children.
Nice to have
• Artistic effect to complement Australian cover.
Subtle retro feel to complement Australian cover.
Should not have
• The book is inclusive of all parents (including same-sex parents) so no images of mother/father and baby.

```html
<!DOCTYPE html>
<html lang="en">
<head>
<meta charset="utf-8">
<title>Rooted Together: 7 Paths to Raise a Household that Blooms</title>
<link rel="stylesheet" href="https://fonts.googleapis.com/css2?family=Anton&family=Lobster&display=swap">
<style>
  :root {
    --linen-light: #f6cf72;
    --linen-mid: #ecbc57;
    --linen-deep: #d9a444;
    --tree-shade: rgba(150, 110, 50, 0.42);
    --title-blue: #1537c9;
    --title-edge: #f7e27a;
    --block-orange: #c8650c;
    --leaf-green: #1f9d0c;
    --leaf-edge: #0c7a06;
    --glow: #f2ffd8;
  }
  html, body {
    margin: 0;
    padding: 0;
    overflow: hidden;
    background: var(--linen-mid);
  }
  .cover {
    position: relative;
    width: 846px;
    height: 1200px;
    overflow: hidden;
    background: linear-gradient(180deg, var(--linen-light) 0%, var(--linen-mid) 55%, var(--linen-deep) 100%);
  }
  .tree-art {
    position: absolute;
    inset: 0;
    background:
      radial-gradient(ellipse 46% 30% at 50% 33%, var(--tree-shade) 0%, rgba(150,110,50,0.18) 60%, transparent 100%),
      linear-gradient(90deg, transparent 41%, var(--tree-shade) 46%, var(--tree-shade) 52%, transparent 57%) 0 620px / 100% 580px no-repeat;
  }
  .series-title {
    position: absolute;
    left: 0;
    top: 165px;
    width: 846px;
    margin: 0;
    text-align: center;
    font-family: "Lobster", cursive;
    font-weight: 400;
    font-style: italic;
    font-size: 92px;
    line-height: 1;
    color: var(--title-blue);
    -webkit-text-stroke: 2px var(--title-edge);
    paint-order: stroke fill;
    text-shadow: 0 0 3px rgba(255, 240, 150, 0.8);
  }
  .subtitle-block {
    position: absolute;
    left: 94px;
    top: 362px;
    width: 660px;
    height: 512px;
    background: var(--block-orange);
    filter: blur(14px);
    opacity: 0.95;
  }
  .subtitle {
    position: absolute;
    left: 0;
    top: 0;
    width: 846px;
    height: 1200px;
  }
  .subtitle-line {
    font-family: "Anton", sans-serif;
    fill: var(--leaf-green);
  }
  .subtitle-glow .subtitle-line {
    fill: var(--glow);
    stroke: var(--glow);
    stroke-width: 14px;
    stroke-linejoin: round;
  }
  .subtitle-face .subtitle-line {
    stroke: var(--leaf-edge);
    stroke-width: 2px;
  }
</style>
</head>
<body>
  <main class="cover">
    <div class="tree-art" role="img" aria-label="Faint illustrated tree with spreading branches and trunk behind the title"></div>

    <h1 class="series-title">Rooted Together:</h1>

    <div class="subtitle-block"></div>

    <svg class="subtitle" viewBox="0 0 846 1200" aria-label="7 Paths to Raise a Household that Blooms">
      <defs>
        <filter id="soft-glow" x="-10%" y="-10%" width="120%" height="120%">
          <feGaussianBlur stdDeviation="4"/>
        </filter>
      </defs>
      <g class="subtitle-glow" filter="url(#soft-glow)" aria-hidden="true">
        <text class="subtitle-line" x="90" y="494" font-size="128" textLength="664" lengthAdjust="spacingAndGlyphs">7 PATHS TO</text>
        <text class="subtitle-line" x="90" y="636" font-size="160" textLength="664" lengthAdjust="spacingAndGlyphs">RAISE</text>
        <text class="subtitle-line" x="90" y="726" font-size="98" textLength="664" lengthAdjust="spacingAndGlyphs">A HOUSEHOLD THAT</text>
        <text class="subtitle-line" x="90" y="852" font-size="142" textLength="664" lengthAdjust="spacingAndGlyphs">BLOOMS</text>
      </g>
      <g class="subtitle-face">
        <text class="subtitle-line" x="90" y="494" font-size="128" textLength="664" lengthAdjust="spacingAndGlyphs">7 PATHS TO</text>
        <text class="subtitle-line" x="90" y="636" font-size="160" textLength="664" lengthAdjust="spacingAndGlyphs">RAISE</text>
        <text class="subtitle-line" x="90" y="726" font-size="98" textLength="664" lengthAdjust="spacingAndGlyphs">A HOUSEHOLD THAT</text>
        <text class="subtitle-line" x="90" y="852" font-size="142" textLength="664" lengthAdjust="spacingAndGlyphs">BLOOMS</text>
      </g>
    </svg>
  </main>
</body>
</html>
```